I am looking for a bottle design for a new start-up olive oil & balsamic vinegar retail store.
I am a specialty store specializing in extra virgin olive oils/infused olive oil and aged and infused balsamic vinegars.
I would like to see designs that celebrate life/food & especially superior olive oil along with the edginess & artistic community of Williamsburg, Brooklyn, New York where my store will be located.
The bottle design must be 1 color (can be white) over a dark green bottle. Bottle sizes are 200ml/375ml/750ml

Artwork design dimensions:
(front or back)

200ml
Maximum width – 2.50 inches
Maximum height – 4.25 inches

375ml
Maximum width – 3.25 inches
Maximum height – 4.50 inches

750ml
Maximum width – 3.625 inches
Maximum height – 6.50 inches

Delivery:
Adobe Illustrator or EPS file delivery.
Updates

Designers. This will not be on a paper label but screened onto a dark green bottle.

No backgrounds needed.

Thanks,
Verde Kettle

Target Market(s)

Foodies/hipsters/People who eat healthy & locally

Industry/Entity Type

Retail

Requirements
Must have
• The bottle have the following information on the front.

VERDE
KETTLE (name of store)

Pure extra virgin olive oil
&
Balsamic Vinegar

14 Tamsen Row
Williamsburg
718-555-0172
verdekettle.example

ml/oz

On the back must have:

Supplied by
Harrowgate Pantry Company
Oakland, CA
510-555-0148
Nice to have
• olives/olive trees or branches. Can be an artistic representation.
Not necessary to have image.

```html
<!DOCTYPE html>
<html lang="en">
<head>
<meta charset="utf-8">
<title>Verde Kettle — Bottle Print 200ml</title>
<link rel="stylesheet" href="https://fonts.googleapis.com/css2?family=Barlow+Semi+Condensed:wght@400;500;600;700&display=swap">
<style>
  :root {
    --bottle-green: #1a3d09;
    --bottle-green-deep: #123806;
    --ink-white: #ffffff;
    --ink-green: #183a0b;
  }
  html, body {
    margin: 0;
    padding: 0;
    width: 1200px;
    height: 900px;
    overflow: hidden;
  }
  body {
    font-family: "Barlow Semi Condensed", "Arial Narrow", sans-serif;
  }
  .bottle-face {
    position: relative;
    width: 1200px;
    height: 900px;
    background: linear-gradient(180deg, var(--bottle-green-deep) 0%, var(--bottle-green) 100%);
    color: var(--ink-white);
  }
  .product-title {
    position: absolute;
    left: 385px;
    top: 50px;
    margin: 0;
    font-weight: 600;
    font-size: 52px;
    line-height: 52px;
    letter-spacing: 0.2px;
    text-transform: uppercase;
  }
  .label-panel {
    position: absolute;
    left: 384px;
    top: 263px;
    width: 432px;
    height: 485px;
    background: var(--ink-white);
    color: var(--ink-green);
    overflow: hidden;
  }
  .branch-art {
    position: absolute;
    right: 0;
    top: 0;
  }
  .store-name {
    position: absolute;
    left: 16px;
    top: 16px;
    margin: 0;
    font-weight: 700;
    font-size: 46px;
    line-height: 51px;
  }
  .store-offer {
    position: absolute;
    left: 16px;
    top: 118px;
    margin: 0;
    font-weight: 400;
    font-size: 46px;
    line-height: 51.5px;
  }
  .store-web {
    position: absolute;
    right: 12px;
    bottom: 6px;
    margin: 0;
    font-weight: 500;
    font-size: 21px;
  }
  .store-contact {
    position: absolute;
    left: 385px;
    top: 760px;
    width: 432px;
    margin: 0;
    font-weight: 600;
    font-size: 19.5px;
    letter-spacing: 0.2px;
    white-space: nowrap;
  }
  .store-contact .divider { margin: 0 8px; font-weight: 400; }
  .volume {
    position: absolute;
    right: 384px;
    top: 825px;
    margin: 0;
    font-weight: 500;
    font-size: 23px;
  }
</style>
</head>
<body>
  <main class="bottle-face">
    <h1 class="product-title">Pure<br>Extra Virgin<br>Olive Oil</h1>

    <section class="label-panel">
      <svg class="branch-art" width="230" height="385" viewBox="0 0 230 385" role="img" aria-label="Olive branch with leaves and olives">
        <defs>
          <linearGradient id="branchTone" x1="0" y1="0" x2="1" y2="1">
            <stop offset="0" stop-color="#1f4510"/>
            <stop offset="1" stop-color="#183a0b"/>
          </linearGradient>
        </defs>
        <rect x="0" y="0" width="230" height="385" fill="url(#branchTone)"/>
      </svg>

      <h2 class="store-name">VERDE<br>KETTLE</h2>
      <p class="store-offer">PURE<br>EXTRA<br>VIRGIN<br>OLIVE OIL<br>&amp;<br>BALSAMIC<br>VINEGAR</p>
      <p class="store-web">verdekettle.example</p>
    </section>

    <p class="store-contact">14 TAMSEN ROW<span class="divider">|</span>WILLIAMSBURG<span class="divider">|</span>718-555-0172</p>
    <p class="volume">200ml/6.7oz</p>
  </main>
</body>
</html>
```